Sales banner for E-commerce

This banner is intended for an e-commerce site selling motorcycle equipment and accessories.
The banner announces the sales and leads the customer to an offer of helmets, equipment, and accessories for motorcyclists.
The style of the banner must be modern, elegant, and both show that the prices are attractive and make you want to click to discover the offer of sale products behind it.
I insist on the aesthetics and the marketing side of the banner which are two absolutely essential elements.
Banner format 3840 (W) x 1250 (H)
Updates
Faible participation designers
Target Market(s)
Biker clientele in the general sense
Industry/Entity Type
Ecommerce Equipement et accessoires moto
Requirements
Must have
- Represent or inspire the motorcycle universe.
Nice to have
- The banner must be attractive and make you want to click

```html
<!DOCTYPE html>
<html lang="en">
<head>
<meta charset="UTF-8">
<title>Sale Banner – 25% Off Helmets</title>
<link href="https://fonts.googleapis.com/css2?family=Roboto:wght@300;400;700&display=swap" rel="stylesheet">
<style>
  :root {
    --page-bg: #ffffff;
    --sale-red: #c41e26;
    --sale-red-light: #cc2a31;
    --sale-red-dark: #b3171f;
    --night: #000000;
    --white: #ffffff;
    --price-red: #d6303b;
    --old-price: #d9d9d9;
    --helmet-light: #4a4a4a;
    --helmet-mid: #262626;
    --helmet-dark: #0c0c0c;
  }
  * { margin: 0; padding: 0; box-sizing: border-box; }
  html, body {
    width: 1200px;
    height: 1000px;
    overflow: hidden;
    background: var(--page-bg);
    font-family: "Roboto", Arial, sans-serif;
  }
  .banner {
    position: absolute;
    left: 24px;
    top: 313px;
    width: 1152px;
    height: 375px;
    display: flex;
  }
  .promo-panel {
    position: relative;
    width: 491px;
    height: 100%;
    background: linear-gradient(120deg, var(--sale-red-light) 0%, var(--sale-red) 45%, var(--sale-red-dark) 100%);
  }
  .headline {
    position: absolute;
    right: 18px;
    text-align: right;
    color: var(--white);
    text-shadow: 4px 5px 6px rgba(0, 0, 0, 0.35);
    line-height: 1;
    white-space: nowrap;
  }
  .headline--sale {
    top: 37px;
    font-size: 157px;
    font-weight: 300;
    letter-spacing: -2px;
  }
  .headline--discount {
    top: 185px;
    font-size: 98px;
    font-weight: 400;
    letter-spacing: -4px;
  }
  .cta-button {
    position: absolute;
    left: 228px;
    top: 296px;
    width: 128px;
    height: 34px;
    border-radius: 17px;
    background: var(--white);
    color: var(--sale-red);
    font-size: 15px;
    font-weight: 700;
    display: flex;
    align-items: center;
    justify-content: center;
    text-decoration: none;
    box-shadow: 3px 4px 6px rgba(0, 0, 0, 0.35);
  }
  .product-panel {
    position: relative;
    flex: 1;
    height: 100%;
    background: var(--night);
  }
  .product-visual {
    position: absolute;
    left: 137px;
    top: 17px;
    width: 334px;
    height: 345px;
    border-radius: 55% 45% 35% 30% / 40% 40% 55% 60%;
    background: radial-gradient(ellipse at 40% 30%, var(--helmet-light) 0%, var(--helmet-mid) 45%, var(--helmet-dark) 100%);
  }
  .price {
    position: absolute;
    right: 536px;
    text-align: right;
    white-space: nowrap;
    line-height: 1;
  }
  .price--now {
    top: 279px;
    color: var(--price-red);
    font-size: 30px;
    font-weight: 700;
  }
  .price--was {
    top: 313px;
    color: var(--old-price);
    font-size: 21px;
    font-weight: 400;
    text-decoration: line-through;
  }
</style>
</head>
<body>
  <section class="banner">
    <div class="promo-panel" role="img" aria-label="Red carbon-fibre weave background">
      <h1 class="headline headline--sale">SALE</h1>
      <p class="headline headline--discount">25% OFF</p>
      <a class="cta-button" href="#">SHOP NOW</a>
    </div>
    <div class="product-panel">
      <div class="product-visual" role="img" aria-label="Black carbon-fibre full-face motorcycle helmet with dark visor, three-quarter side view"></div>
      <p class="price price--now">419.92€</p>
      <p class="price price--was">559.90€</p>
    </div>
  </section>
</body>
</html>
```